Business Card Design Project

Hello
I want a Simple Business card that uses the company logo that is easily reasonable but looks professional as I am an IT Services company and would look to share these cards with prospective clients.
The details are:
Kelvo Ridge Solutions
14 Marlow Crescent
Birmingham
B7 4QT
Telephone 0845 271 6049
I would like my name Gareth Wilcombe and my title Director on the card.
Target Market(s)
IT Professionals
Industry/Entity Type
Business

```html
<!DOCTYPE html>
<html lang="en">
<head>
<meta charset="utf-8">
<title>Kelvo Ridge Solutions — Business Card</title>
<link rel="stylesheet" href="https://fonts.googleapis.com/css2?family=Questrial&family=Roboto:wght@300;400&display=swap">
<style>
  :root {
    --backdrop: #e9e9e7;
    --card: #ffffff;
    --ink: #2f2f36;
    --ink-soft: #5a5a60;
    --leaf: #8fcf7a;
    --icon-green: #7cbf6a;
    --icon-yellow: #e8c84a;
  }
  * { box-sizing: border-box; margin: 0; padding: 0; }
  html, body {
    width: 1200px;
    height: 1000px;
    overflow: hidden;
    background: var(--backdrop);
  }
  .card {
    position: absolute;
    left: 145px;
    top: 240px;
    width: 910px;
    height: 520px;
    background: var(--card);
    box-shadow: 0 2px 10px rgba(0,0,0,0.08);
  }
  .brand {
    position: absolute;
    left: 80px;
    top: 190px;
    display: flex;
    align-items: center;
    gap: 18px;
  }
  .brand-dot {
    width: 34px;
    height: 34px;
    border-radius: 50%;
    background: var(--leaf);
  }
  .brand-name {
    font-family: 'Questrial', sans-serif;
    font-size: 46px;
    color: var(--ink);
    letter-spacing: 0.5px;
  }
  .person {
    position: absolute;
    right: 80px;
    top: 210px;
    text-align: center;
  }
  .person-name {
    font-family: 'Roboto', sans-serif;
    font-weight: 400;
    font-size: 30px;
    color: var(--ink);
  }
  .person-title {
    font-family: 'Roboto', sans-serif;
    font-weight: 300;
    font-size: 14px;
    letter-spacing: 1px;
    color: var(--ink-soft);
    margin-top: 6px;
  }
  .contact {
    position: absolute;
    left: 620px;
    top: 330px;
    list-style: none;
    font-family: 'Roboto', sans-serif;
    font-weight: 300;
    font-size: 16px;
    line-height: 1.2;
    color: var(--ink-soft);
  }
  .contact-item {
    display: flex;
    align-items: flex-start;
    gap: 10px;
    margin-bottom: 14px;
  }
  .contact-icon { width: 18px; height: 18px; flex: none; margin-top: 1px; }
</style>
</head>
<body>
  <main class="card">
    <div class="brand">
      <span class="brand-dot"></span>
      <span class="brand-name">Kelvo Ridge Solutions</span>
    </div>

    <div class="person">
      <p class="person-name">Gareth Wilcombe</p>
      <p class="person-title">DIRECTOR</p>
    </div>

    <ul class="contact">
      <li class="contact-item">
        <svg class="contact-icon" viewBox="0 0 18 18" aria-hidden="true">
          <path d="M2 9 L9 3 L16 9 M4 8 V15 H14 V8" fill="none" stroke="var(--icon-green)" stroke-width="1.6"/>
        </svg>
        <span>14 Marlow Crescent<br>Birmingham<br>B7 4QT</span>
      </li>
      <li class="contact-item">
        <svg class="contact-icon" viewBox="0 0 18 18" aria-hidden="true">
          <rect x="5" y="2" width="8" height="14" rx="1.5" fill="none" stroke="var(--icon-green)" stroke-width="1.6"/>
          <line x1="7" y1="13" x2="11" y2="13" stroke="var(--icon-green)" stroke-width="1.4"/>
        </svg>
        <span>0845 271 6049</span>
      </li>
      <li class="contact-item">
        <svg class="contact-icon" viewBox="0 0 18 18" aria-hidden="true">
          <rect x="1.5" y="4" width="15" height="10" fill="none" stroke="var(--icon-yellow)" stroke-width="1.5"/>
          <path d="M1.5 4 L9 10 L16.5 4" fill="none" stroke="var(--icon-yellow)" stroke-width="1.5"/>
        </svg>
        <span>director@kelvoridge.net</span>
      </li>
    </ul>
  </main>
</body>
</html>
```